Professional window cleaning services business needs a flyer design

We are looking to attract large businesses such as gyms, car dealerships and fast food restaurants.
-Have over 15 years of experience in this business
-We serve customers in Melbourne and all surrounding suburbs
-Specialising in automated periodical services(daily,weekly,monthly, yearly)
-Our current client base consists of major fast food restaurants, car dealerships and residential properties.

Industry/Entity Type

Window Cleaning

Colors
3176b5
fbed22

Requirements
Must have
• Business Details:
• Name: Brightpane Window Cleaning
• Phone no:95402367
• website:www.quorlinpro.com.au
• email: admin@quorlinpro.com.au
• mail: PO BOX 4826, Marrowdale Heights, 3478

```html
<!DOCTYPE html>
<html lang="en">
<head>
<meta charset="utf-8">
<title>Brightpane Window Cleaning Flyer</title>
<link href="https://fonts.googleapis.com/css2?family=Arimo:wght@400;700&family=Roboto+Condensed:wght@400;700&display=swap" rel="stylesheet">
<style>
  :root {
    --brand-blue: #3176b5;
    --text-blue: #2c6db2;
    --brand-yellow: #fbed22;
    --white: #ffffff;
    --cap-white: #eef0f2;
    --overall-blue: #3a68a6;
    --skin: #f3c7a8;
  }
  html, body {
    margin: 0;
    padding: 0;
    overflow: hidden;
    background: var(--white);
  }
  .flyer {
    position: relative;
    width: 1200px;
    height: 857px;
    overflow: hidden;
    background: var(--white);
    font-family: "Arimo", Arial, sans-serif;
  }
  .hero-illustration {
    position: absolute;
    left: 0;
    top: 40px;
    width: 600px;
    height: 560px;
    border-radius: 46% 46% 18px 18px / 38% 38% 18px 18px;
    background: linear-gradient(180deg,
      var(--cap-white) 0%,
      #c9d6e8 12%,
      var(--overall-blue) 20%,
      var(--skin) 34%,
      #f6d5bd 52%,
      #e8ecf1 62%,
      var(--overall-blue) 72%,
      #4a78b3 84%,
      var(--skin) 94%,
      #f6dcc8 100%);
  }
  .phone-box {
    position: absolute;
    left: 378px;
    top: 545px;
    width: 233px;
    height: 77px;
    background: var(--brand-yellow);
    text-align: center;
  }
  .phone-number {
    display: block;
    font-family: "Roboto Condensed", "Arial Narrow", sans-serif;
    font-weight: 700;
    font-size: 52px;
    line-height: 54px;
    margin-top: 3px;
    color: var(--text-blue);
  }
  .phone-email {
    display: block;
    font-size: 13px;
    color: var(--text-blue);
    line-height: 14px;
  }
  .about {
    position: absolute;
    left: 25px;
    top: 634px;
    width: 585px;
    margin: 0;
    font-size: 16px;
    line-height: 22.9px;
    letter-spacing: -0.6px;
    white-space: nowrap;
    color: var(--text-blue);
  }
  .side-panel {
    position: absolute;
    left: 619px;
    top: 0;
    width: 581px;
    height: 857px;
    background: var(--brand-blue);
  }
  .wordmark {
    position: absolute;
    left: 0;
    top: 36px;
    width: 100%;
    text-align: center;
    font-family: "Roboto Condensed", "Arial Narrow", sans-serif;
    font-weight: 700;
    font-size: 76px;
    line-height: 90px;
    color: var(--brand-yellow);
  }
  .company-name {
    position: absolute;
    left: 0;
    top: 160px;
    width: 100%;
    text-align: center;
    margin: 0;
    font-weight: 400;
    font-size: 38px;
    letter-spacing: -0.8px;
    color: var(--white);
  }
  .tagline {
    position: absolute;
    left: 0;
    top: 224px;
    width: 100%;
    text-align: center;
    margin: 0;
    font-size: 19px;
    letter-spacing: -0.5px;
    color: var(--brand-yellow);
  }
  .features {
    position: absolute;
    left: 113px;
    top: 276px;
    margin: 0;
    padding: 0;
    list-style: none;
    color: var(--white);
    font-size: 22px;
    letter-spacing: -0.4px;
  }
  .features li {
    position: relative;
    padding-left: 29px;
    line-height: 28px;
    margin-bottom: 9px;
  }
  .features li.first { margin-bottom: 0; }
  .features li.two-line { margin-bottom: 10px; }
  .tick {
    position: absolute;
    left: 0;
    top: 6px;
    width: 20px;
    height: 18px;
  }
  .van-photo {
    position: absolute;
    left: 62px;
    top: 482px;
    width: 492px;
    height: 258px;
    border: 2px solid var(--white);
    background: linear-gradient(180deg, #c9ccc7 0%, #9aa193 35%, #f1d83a 55%, #e9cc25 78%, #6c6f6a 100%);
  }
  .postal {
    position: absolute;
    left: 0;
    top: 757px;
    width: 100%;
    text-align: center;
    font-family: "Roboto Condensed", "Arial Narrow", sans-serif;
    font-weight: 700;
    font-size: 27px;
    color: var(--white);
  }
  .website {
    position: absolute;
    left: 0;
    top: 801px;
    width: 100%;
    text-align: center;
    font-family: "Roboto Condensed", "Arial Narrow", sans-serif;
    font-size: 34px;
    letter-spacing: 2.6px;
    color: var(--brand-yellow);
  }
</style>
</head>
<body>
<div class="flyer">
  <div class="hero-illustration" role="img" aria-label="Cartoon window cleaner in cap and overalls holding a squeegee and pointing down at the phone number"></div>

  <div class="phone-box">
    <span class="phone-number">95402367</span>
    <span class="phone-email">admin@quorlinpro.com.au</span>
  </div>

  <p class="about">Brightpane Services started trading in 1999 with a clear focus on becoming a market<br>leader in the Window Cleaning Industry. Since then we have proudly built the<br>business based on strong ethical standards, focused on customer service.<br>With this viewpoint in mind we have built a reputation for fast, efficient service<br>that has paved the way for us to become one of the leaders in window cleaning<br>in Melbourne. Our clients now range from big corporate jobs such as stadiums<br>and office buildings, to shop fronts to residential. Our scaled pricing allows us to<br>be competitive in all markets.</p>

  <aside class="side-panel">
    <div class="wordmark">BRIGHTPANE</div>
    <h1 class="company-name">Brightpane Window Cleaning</h1>
    <p class="tagline">Melbourne's Premier Window Cleaning Company</p>

    <ul class="features">
      <li class="first"><svg class="tick" viewBox="0 0 20 18"><path d="M1 10 L7 16 L19 2" fill="none" stroke="#fbed22" stroke-width="3.5" stroke-linecap="round" stroke-linejoin="round"/></svg>15 years of experience in this business</li>
      <li class="two-line"><svg class="tick" viewBox="0 0 20 18"><path d="M1 10 L7 16 L19 2" fill="none" stroke="#fbed22" stroke-width="3.5" stroke-linecap="round" stroke-linejoin="round"/></svg>Specialising in automated periodical services<br>(daily,weekly,monthly, yearly)</li>
      <li><svg class="tick" viewBox="0 0 20 18"><path d="M1 10 L7 16 L19 2" fill="none" stroke="#fbed22" stroke-width="3.5" stroke-linecap="round" stroke-linejoin="round"/></svg>Residential Window Cleaning</li>
      <li><svg class="tick" viewBox="0 0 20 18"><path d="M1 10 L7 16 L19 2" fill="none" stroke="#fbed22" stroke-width="3.5" stroke-linecap="round" stroke-linejoin="round"/></svg>Commercial Window Cleaning</li>
      <li><svg class="tick" viewBox="0 0 20 18"><path d="M1 10 L7 16 L19 2" fill="none" stroke="#fbed22" stroke-width="3.5" stroke-linecap="round" stroke-linejoin="round"/></svg>Real Estate Window Cleaning</li>
    </ul>

    <div class="van-photo" role="img" aria-label="Photo of a cleaner standing beside the yellow company van with ladders on the roof rack"></div>

    <div class="postal">PO BOX 4826, Marrowdale Heights, 3478</div>
    <div class="website">www.quorlinpro.com.au</div>
  </aside>
</div>
</body>
</html>
```